Postcard Design hearing aid sales & service. Free hearing test . Fresh batteries

Cedar Hollow Hearing Aid Device Center . Located at 417 Marlowe Ln Abilene Texas 79605 Ph 325-555-0148.
Hours Mon thru Thurs 9:00am - 5:00pm closed for lunch 12:00pm - 1:00pm . Fri open 9:00am - 1:00pm
Hearing Test n/c Hearing aid adjustment & cleaning of hearing aids n/c . Fresh batteries buy one 1/2 off on 2nd pack. Limited time. Walk-in welcome Appointments appreciated. THIS MONTH ONLY Special discounts on new state of the art hearing aids w/remote. .

```html
<!DOCTYPE html>
<html lang="en">
<head>
<meta charset="utf-8">
<title>Cedar Hollow Hearing Aid Device Center — Postcard</title>
<link href="https://fonts.googleapis.com/css2?family=Lato:wght@400;700;900&family=Roboto+Condensed:wght@700&family=Tinos:wght@700&display=swap" rel="stylesheet">
<style>
  :root{
    --backdrop:#6a4829;
    --card:#ffffff;
    --charcoal:#2f2f31;
    --red:#d8232f;
    --red-dark:#b51822;
    --ink:#1d1d1d;
    --rule:#bdbdbd;
  }
  *{box-sizing:border-box;margin:0;padding:0}
  html,body{width:907px;height:1200px;overflow:hidden}
  body{background:var(--backdrop);position:relative;font-family:"Lato",sans-serif}
  .postcard{position:absolute;width:662px;height:515px;background:var(--card);overflow:hidden}
  .postcard--front{left:118px;top:50px}
  .postcard--back{left:118px;top:626px}
  .postcard__art{position:absolute;inset:0}
  .postcard__art svg{display:block}

  .brand{position:absolute;left:19px;top:23px;font-family:"Tinos",serif;font-weight:700;font-size:18px;color:var(--red);white-space:nowrap}
  .headline{position:absolute;left:18px;top:66px;font-family:"Roboto Condensed",sans-serif;font-weight:700;color:#fff;line-height:1}
  .headline__main{font-size:39px;display:block}
  .headline__sub{font-size:23px;display:block;margin-top:10px}

  .tab{position:absolute;left:0;height:24px;padding:0 18px 0 17px;background:var(--red);color:#fff;font-weight:700;font-size:17px;line-height:24px;border-radius:0 12px 12px 0}
  .tab--service{top:158px}
  .tab--schedule{top:325px;height:25px;line-height:25px}
  .tab--about{top:267px}

  .service-list{position:absolute;left:20px;top:192px;list-style:none;font-size:13px;color:var(--ink)}
  .service-list li{position:relative;padding-left:27px;height:26px;line-height:17px}
  .service-list li::before{content:"";position:absolute;left:0;top:6px;width:6px;height:6px;border-radius:50%;background:#111}
  .service-list li.two-line{height:auto}

  .schedule{position:absolute;left:24px;top:357px;list-style:none;font-size:13px;color:#fff;line-height:17px}
  .schedule li{position:relative;padding-left:23px;margin-bottom:5px}
  .schedule li::before{content:"";position:absolute;left:0;top:6px;width:6px;height:6px;border-radius:50%;background:var(--red)}
  .schedule .day{color:var(--red)}

  .offer{position:absolute;left:12px;top:428px;width:300px;height:42px;border-radius:21px;background:linear-gradient(#e23a44,var(--red-dark));padding:3px}
  .offer__inner{height:100%;border:2px dotted #fff;border-radius:18px;color:#fff;font-size:12px;line-height:15px;padding:3px 8px 3px 10px;white-space:nowrap}

  .call{position:absolute;left:21px;top:486px;font-size:13px;color:var(--ink)}
  .call__phone{color:var(--red);margin-left:18px}

  .about{position:absolute;left:17px;top:296px;width:330px;font-size:12px;line-height:16px;color:#fff;text-align:justify}
  .contact-title{position:absolute;left:17px;top:430px;font-size:12.5px;font-weight:700;color:var(--red)}
  .contact{position:absolute;left:17px;font-size:13px;color:#fff;display:flex;align-items:center;gap:7px}
  .contact--address{top:453px}
  .contact--phone{top:477px}
  .contact svg{width:12px;height:12px;fill:#fff}

  .stamp{position:absolute;left:583px;top:34px;width:56px;height:64px;border:1.5px solid #9a9a9a}
  .address-line{position:absolute;left:434px;width:198px;height:1px;background:var(--rule)}
</style>
</head>
<body>

<section class="postcard postcard--front">
  <div class="postcard__art">
    <svg width="662" height="515" viewBox="0 0 662 515">
      <defs>
        <linearGradient id="darkPanel" x1="0" y1="0" x2="0" y2="1">
          <stop offset="0" stop-color="#3a3a3d"/><stop offset="1" stop-color="#262628"/>
        </linearGradient>
        <linearGradient id="portraitTone" x1="0" y1="0" x2="1" y2="1">
          <stop offset="0" stop-color="#f3ece7"/><stop offset=".45" stop-color="#d8a98e"/><stop offset=".75" stop-color="#8a5a3f"/><stop offset="1" stop-color="#e4866f"/>
        </linearGradient>
      </defs>
      <rect x="0" y="58" width="430" height="124" fill="url(#darkPanel)"/>
      <rect x="0" y="180" width="430" height="4" fill="var(--red)"/>
      <rect x="0" y="310" width="430" height="4" fill="var(--red)"/>
      <rect x="0" y="314" width="430" height="170" fill="url(#darkPanel)"/>
      <circle cx="597" cy="280" r="325" fill="var(--red)"/>
      <circle cx="606" cy="280" r="318" fill="#fff"/>
      <circle cx="608" cy="280" r="311" fill="url(#portraitTone)" role="img" aria-label="Photo of a woman cupping her hand to her ear to listen"/>
    </svg>
  </div>

  <div class="brand">Cedar Hollow Hearing Aid Device Center</div>
  <h1 class="headline">
    <span class="headline__main">Walk-in welcome</span>
    <span class="headline__sub">Appointments appreciated</span>
  </h1>

  <div class="tab tab--service">Our Service</div>
  <ul class="service-list">
    <li>Hearing Test</li>
    <li>Hearing aid adjustment</li>
    <li>Cleaning of hearing aids</li>
    <li class="two-line">Fresh batteries buy one 1/2 off<br>on 2nd pack</li>
  </ul>

  <div class="tab tab--schedule">Time Schedule</div>
  <ul class="schedule">
    <li><span class="day">Monday to Thursday</span> 9:00am - 5:00pm<br>(Closed for lunch 12:00pm - 1:00pm)</li>
    <li><span class="day">Friday</span> open 9:00am - 1:00pm</li>
  </ul>

  <div class="offer"><div class="offer__inner">THIS MONTH ONLY Special Discounts on new state<br>of the art hearing aids remote</div></div>

  <p class="call">Call Now for more information <span class="call__phone">325-555-0148.</span></p>
</section>

<section class="postcard postcard--back">
  <div class="postcard__art">
    <svg width="662" height="515" viewBox="0 0 662 515">
      <defs>
        <clipPath id="leftPanel"><path d="M272 0 C450 100 450 330 250 515 L0 515 L0 0 Z"/></clipPath>
        <linearGradient id="fittingTone" x1="0" y1="0" x2="1" y2="0">
          <stop offset="0" stop-color="#d9c9bd"/><stop offset=".35" stop-color="#b98b6d"/><stop offset=".7" stop-color="#e9ddd2"/><stop offset="1" stop-color="#f4f4f4"/>
        </linearGradient>
        <linearGradient id="darkPanelBack" x1="0" y1="0" x2="0" y2="1">
          <stop offset="0" stop-color="#3a3a3d"/><stop offset="1" stop-color="#262628"/>
        </linearGradient>
      </defs>
      <path d="M284 0 C462 100 462 330 262 515 L0 515 L0 0 Z" fill="var(--red)"/>
      <path d="M277 0 C455 100 455 330 255 515 L0 515 L0 0 Z" fill="#fff"/>
      <g clip-path="url(#leftPanel)">
        <rect x="0" y="0" width="460" height="251" fill="url(#fittingTone)" role="img" aria-label="Photo of a specialist fitting a hearing aid on a girl's ear"/>
        <rect x="0" y="251" width="460" height="3" fill="var(--red)"/>
        <rect x="0" y="254" width="460" height="261" fill="url(#darkPanelBack)"/>
      </g>
    </svg>
  </div>

  <div class="tab tab--about">About Us</div>
  <p class="about">Lorem ipsum dolor sit amet, consectetuer adipiscing elit. Aenean commodo ligula eget dolor. Aenean massa. Cum sociis natoque penatibus et magnis dis parturient montes, nascetur ridiculus mus. Donec quam felis, ultricies nec, pellentesque eu, pretium quis, In enim justo, rhoncus ut, imperdiet a, venenatis vitae, justo. Nullam dictum felis eu pede mollis pretium. Integer tincidunt. Cras dapibus.</p>

  <p class="contact-title">Contact Us for more information</p>
  <p class="contact contact--address">
    <svg viewBox="0 0 12 12"><path d="M6 1 L11.5 6 H10 V11 H7.3 V7.8 H4.7 V11 H2 V6 H0.5 Z"/></svg>
    417 Marlowe Ln Abilene Texas79605
  </p>
  <p class="contact contact--phone">
    <svg viewBox="0 0 12 12"><path d="M2.4 1 L4.4 1 L5.2 3.6 L4 4.7 C4.6 6 5.8 7.3 7.3 8 L8.4 6.8 L11 7.6 L11 9.6 C11 10.4 10.4 11 9.6 11 C5 11 1 7 1 2.4 C1 1.6 1.6 1 2.4 1 Z"/></svg>
    325-555-0148
  </p>

  <div class="stamp"></div>
  <div class="address-line" style="top:251px"></div>
  <div class="address-line" style="top:298px"></div>
  <div class="address-line" style="top:345px"></div>
</section>

</body>
</html>
```